LLC needs a business card design that emphasizes consulting and expert witness in upstream oil and g

I need a business card design for my company called Velmo Consultative Service, LLC. My expertise is in oil and gas upstream operations management to optimize performance and also as an expert witness for law firms in oil and gas upstream operations litigation.
The final design should communicate knowledge and hands-on experience as well as trust. (Velmo means rope or lasso. Perhaps "Velmo" should be in the form of a rope.) I do not like the color green in any shade. My first preference would be some shade of blue.

```html
<!DOCTYPE html>
<html lang="en">
<head>
<meta charset="utf-8">
<title>Velmo Consultative Service – Business Card</title>
<link rel="stylesheet" href="https://fonts.googleapis.com/css2?family=Open+Sans:wght@400;600&display=swap">
<style>
  :root {
    --backdrop: #c9c9c9;
    --card-white: #ffffff;
    --rope-blue: #0f5f93;
    --accent-blue: #1f79b8;
    --ink: #2b2b2b;
    --photo-dark: #16191c;
    --photo-mid: #26404f;
    --photo-teal: #2e5a72;
  }
  * { margin: 0; padding: 0; box-sizing: border-box; }
  html, body {
    width: 1200px;
    height: 800px;
    overflow: hidden;
    background: var(--backdrop);
    font-family: "Open Sans", Arial, sans-serif;
  }
  .canvas {
    position: relative;
    width: 1200px;
    height: 800px;
  }
  .card {
    position: absolute;
    top: 250px;
    width: 520px;
    height: 300px;
    overflow: hidden;
    box-shadow: 0 6px 14px rgba(0,0,0,0.18);
  }
  .card--front { left: 50px; }
  .card--back { left: 630px; background: var(--card-white); }

  .front-photo {
    position: absolute;
    inset: 0;
    background:
      radial-gradient(ellipse at 70% 65%, var(--photo-teal) 0%, transparent 60%),
      linear-gradient(135deg, var(--photo-dark) 0%, var(--photo-mid) 55%, var(--photo-teal) 100%);
  }
  .front-name {
    position: absolute;
    left: 0;
    right: 0;
    top: 50%;
    transform: translateY(-50%);
    text-align: center;
    color: var(--card-white);
    font-size: 22px;
    font-weight: 600;
    letter-spacing: 1px;
    white-space: nowrap;
  }

  .rope-arc {
    position: absolute;
    inset: 0;
    width: 520px;
    height: 300px;
  }
  .contact {
    position: absolute;
    left: 95px;
    top: 160px;
    color: var(--ink);
  }
  .contact__name { font-size: 21px; font-weight: 400; line-height: 1.2; }
  .contact__position {
    font-size: 10px;
    font-weight: 600;
    letter-spacing: 2.5px;
    color: var(--accent-blue);
    margin: 2px 0 0 12px;
  }
  .contact__list {
    list-style: none;
    margin: 14px 0 0 26px;
    font-size: 13px;
    line-height: 1.6;
  }
  .contact__label {
    display: inline-block;
    width: 16px;
    font-size: 10px;
    font-weight: 600;
    color: var(--accent-blue);
  }
</style>
</head>
<body>
<main class="canvas">
  <section class="card card--front" aria-label="Card front">
    <div class="front-photo" role="img" aria-label="Close-up photograph of a frayed rope in dark blue tones"></div>
    <p class="front-name">Velmo Consultative Service</p>
  </section>

  <section class="card card--back" aria-label="Card back">
    <svg class="rope-arc" viewBox="0 0 520 300" role="img" aria-label="Blue band arching across the card">
      <path d="M 18 310 C 40 150, 140 40, 290 38 C 400 36, 480 60, 540 90"
            fill="none" stroke="var(--rope-blue)" stroke-width="24"/>
    </svg>
    <div class="contact">
      <p class="contact__name">Name Surname</p>
      <p class="contact__position">POSITION</p>
      <ul class="contact__list">
        <li><span class="contact__label">M</span>+00 00 000 00 00</li>
        <li><span class="contact__label">E</span>name.surname@velmo.com</li>
        <li><span class="contact__label">W</span>www.velmo.com</li>
      </ul>
    </div>
  </section>
</main>
</body>
</html>
```